New Website design 2024: Ridgeline Flameguard, Inc.

1. Who we are: At Ridgeline Flameguard Inc, our mission is to provide our clients with comprehensive firestop and seismic expansion joint solutions that ensure the safety and integrity of their buildings. We specialize in the installation of firestop systems at penetrations, wall joints, and slab edge joints, as well as providing acoustical sealants, security sealants, architectural caulking, and seismic expansion joints. Since our establishment in 2007, we have been committed to improving the safety and integrity of buildings through our expertise and use of tested and approved firestop systems. Our focus is to deliver exceptional service and quality workmanship to ensure the protection of lives and property.
2. Services we provide:
-Firestopping: T-ratings, CMU Wall Joint, Exterior Caulking, Fireproof Patching, Head of Wall Joints, Through Penetrations, Curtain Wall/Slab Edge, Grease & Fume Duct Protection.
-Expansion Joints: Floor Covers, Roof Covers, Fire Barriers, Vapor Barriers, Wall & Ceiling Covers, Compression Seals, Pre-Compression Foams, Photoluminescent Signage
3. Examples of scope and projects we’ve completed.
4. How to contact us.: https://ridgelineflameguard.example/contact/
- Social Media Links: https://www.linkedin.example/company/ridgeline-flameguard/mycompany/
https://www.instagram.example/ridgelineflameguard/?hl=en
https://www.youtube.example/channel/UCQ8M2RT5KwpZdNvTeLoJbHs/videos
Target Market(s)
Commercial Construction industry
Industry/Entity Type
Commercial Construction industry in California
Coding
Coded - Design and coding required
Number of Pages Required
4 page
Colors
Designer to choose colors to be used in the design.
Requirements
Must have
- 1. Who we are. 2. Services we provide. 3. Examples of scope and projects we’ve completed. 4. How to contact us.
Nice to have
- Logo. Pictures of scope of work and pictures of projects completed or working on.
Should not have
- Names of clients.

```html
<!DOCTYPE html>
<html lang="en">
<head>
<meta charset="utf-8">
<title>Firestopping – Ridgeline Flameguard, Inc.</title>
<link href="https://fonts.googleapis.com/css2?family=Syncopate:wght@700&family=Montserrat:wght@400;500;600;700&display=swap" rel="stylesheet">
<style>
:root{
  --red:#e30613;
  --blue:#4a5fae;
  --navy:#2c3452;
  --dark:#2a2b2f;
  --ink:#333;
  --muted:#555;
  --line:#e2e2e2;
  --white:#fff;
}
*{box-sizing:border-box;margin:0;padding:0}
html,body{width:1200px;height:2829px;overflow:hidden;background:var(--white)}
body{position:relative;font-family:'Montserrat',sans-serif;color:var(--ink)}
a{color:inherit;text-decoration:none}
.abs{position:absolute}
.display{font-family:'Syncopate',sans-serif;font-weight:700;text-transform:uppercase}
.btn{position:absolute;display:flex;align-items:center;justify-content:center;background:var(--blue);color:var(--white);font-family:'Syncopate',sans-serif;font-weight:700;font-size:10px;letter-spacing:.5px;border-radius:4px;text-transform:uppercase}

/* header */
.site-header{position:absolute;left:0;top:0;width:1200px;height:79px;background:var(--white);z-index:3}
.brand{position:absolute;left:149px;top:12px;display:flex;align-items:center;gap:8px}
.brand-mark{width:22px;height:22px;background:var(--red)}
.brand-name{font-family:'Syncopate',sans-serif;font-weight:700;font-size:19px;color:var(--red);letter-spacing:.5px}
.brand-tag{position:absolute;left:149px;top:56px;font-size:9px;font-weight:700;color:var(--dark);letter-spacing:.6px}
.nav a{position:absolute;top:33px;font-size:12px;letter-spacing:.6px;color:#444;font-weight:500}
.nav a.current{color:var(--red);text-decoration:underline}
.dropdown{position:absolute;left:690px;top:60px;width:140px;z-index:4}
.dropdown a{display:block;height:33px;line-height:33px;padding-left:11px;font-size:12px;color:var(--white);background:var(--blue)}
.dropdown a.current{background:var(--red)}

/* hero */
.hero{position:absolute;left:0;top:79px;width:1200px;height:330px}
.hero-photo{position:absolute;inset:0;background:linear-gradient(100deg,#2b2c2e 0%,#3d3e40 45%,#6b6c6a 70%,#8fa33d 82%,#5a5b58 100%)}
.hero h1{position:absolute;left:149px;top:86px;font-size:40px;font-weight:700;color:var(--white);letter-spacing:.5px}

/* services */
.oct{clip-path:polygon(29% 0,71% 0,100% 29%,100% 71%,71% 100%,29% 100%,0 71%,0 29%)}
.svc{position:absolute;width:184px;text-align:center}
.svc .frame{width:184px;height:184px;background:#e6e6e6;padding:2px}
.svc .photo{width:100%;height:100%}
.svc p{margin-top:12px;font-size:12.5px;letter-spacing:.4px;color:var(--ink);line-height:15px}
.hover-plus{position:absolute;left:77px;top:77px;width:30px;height:30px}

.divider{position:absolute;left:199px;top:1070px;width:800px;height:1px;background:var(--line)}
.section-title{position:absolute;left:0;width:1200px;text-align:center;font-size:24px;color:var(--ink);letter-spacing:1px}
.section-sub{position:absolute;left:0;width:1200px;text-align:center;font-size:12.5px;letter-spacing:.8px;color:var(--muted)}
.video{position:absolute;left:263px;top:1197px;width:674px;height:354px;border:3px solid #e8e8e8;background:linear-gradient(90deg,#e9eaec 0%,#d5d7da 30%,#7c7f83 55%,#a9abae 80%,#55585c 100%)}
.play{position:absolute;left:311px;top:160px;width:50px;height:34px;background:var(--red);border-radius:9px}

/* cta */
.cta-title{position:absolute;left:237px;width:400px;text-align:center;top:1808px;font-size:36px;line-height:42px;color:var(--white);letter-spacing:1px}
.cta-photo{position:absolute;left:648px;top:1663px;width:368px;height:312px;background:linear-gradient(180deg,#3b4360 0%,#4d5570 45%,#d9732e 75%,#e5803a 100%);clip-path:polygon(0 0,100% 0,100% 100%,0 100%)}

/* manufacturers */
.maker{position:absolute;top:2185px;width:144px;height:144px;background:#e8e8e8;padding:2px}
.maker .face{width:100%;height:100%;background:var(--white);display:flex;align-items:center;justify-content:center;text-align:center}
.maker .name{font-family:'Montserrat',sans-serif;font-weight:700;font-size:16px}
.arrow{position:absolute;top:2248px;width:20px;height:20px}

/* footer */
.footer-brand{position:absolute;left:0;width:1200px;top:2512px;text-align:center}
.footer-brand .brand-name{color:var(--white);font-size:24px}
.footer-brand .tag{margin-top:10px;font-size:11px;font-weight:700;color:var(--white);letter-spacing:.8px}
.col-head{position:absolute;top:2608px;font-family:'Syncopate',sans-serif;font-weight:700;font-size:12px;color:var(--red);letter-spacing:.5px;text-transform:uppercase}
.f-text{position:absolute;font-size:12px;color:var(--white);line-height:18px}
.f-link{position:absolute;left:373px;font-size:12px;color:var(--white)}
.f-link.current{color:var(--red);text-decoration:underline}
.icon{position:absolute;left:151px;width:13px;height:13px}
.email{position:absolute;left:565px;top:2671px;width:260px;height:28px;border:1px solid #777;border-radius:3px;font-size:10px;color:#999;padding:7px 12px;background:transparent}
.badge{position:absolute;left:898px}
.legal{position:absolute;left:0;top:2798px;width:1200px;height:31px;background:var(--red)}
.legal p{position:absolute;left:149px;top:9px;font-size:10.5px;color:var(--white)}
.social{position:absolute;top:10px;width:11px;height:11px;background:var(--white);border-radius:2px}
</style>
</head>
<body>

<header class="site-header">
  <a class="brand" href="#"><span class="brand-mark"></span><span class="brand-name">Ridgeline Flameguard</span></a>
  <div class="brand-tag">FIRESTOPPING, INC • EXPANSION JOINTS</div>
  <nav class="nav">
    <a href="#" style="left:570px">WHO WE ARE</a>
    <a href="#" class="current" style="left:690px">WHAT WE DO</a>
    <a href="https://ridgelineflameguard.example/contact/" style="left:810px">CONTACT</a>
  </nav>
  <a class="btn" href="https://ridgelineflameguard.example/contact/" style="left:909px;top:24px;width:142px;height:29px">Quick Inquiry</a>
</header>
<div class="dropdown">
  <a href="#" class="current">Firestopping</a>
  <a href="#">Expansion Joints</a>
  <a href="#">Projects</a>
</div>

<section class="hero">
  <div class="hero-photo" role="img" aria-label="Installer in a high-visibility vest working on a concrete slab"></div>
  <h1>Firestopping</h1>
</section>
<svg class="abs" style="left:0;top:0;z-index:2" width="1200" height="420" viewBox="0 0 1200 420">
  <polygon points="0,255 502,373 1200,255 1200,410 0,410" fill="#fff"/>
  <polygon points="68,277 502,373 1076,280 502,405" fill="#e30613"/>
</svg>

<div class="svc" style="left:202px;top:481px"><div class="frame oct"><div class="photo oct" role="img" aria-label="Insulated pipes with T-rating wrap" style="background:linear-gradient(135deg,#d8d8da,#8c8e92 60%,#4a4a4c)"></div></div><p>T-Ratings</p></div>
<div class="svc" style="left:406px;top:481px"><div class="frame oct"><div class="photo oct" role="img" aria-label="Red sealant along a CMU wall joint" style="background:linear-gradient(180deg,#b9bcc2 0%,#cfd1d6 45%,#c33a2c 55%,#d9d6cf 70%,#e5e3de 100%)"></div></div><p>CMU Wall Joint</p></div>
<div class="svc" style="left:611px;top:481px"><div class="frame oct"><div class="photo oct" role="img" aria-label="Exterior caulking on dark surface" style="background:linear-gradient(135deg,#3a3b3d,#2c2d2f)"></div>
  <svg class="hover-plus" viewBox="0 0 30 30"><circle cx="15" cy="15" r="13" fill="none" stroke="#e30613" stroke-width="2"/><path d="M15 8v14M8 15h14" stroke="#e30613" stroke-width="2"/></svg></div><p>Exterior Caulking</p></div>
<div class="svc" style="left:816px;top:481px"><div class="frame oct"><div class="photo oct" role="img" aria-label="Fireproof patching material on a beam" style="background:linear-gradient(135deg,#e8dfcf,#cbbd9f 55%,#a8987a)"></div></div><p>Fireproof Patching</p></div>

<div class="svc" style="left:202px;top:719px"><div class="frame oct"><div class="photo oct" role="img" aria-label="Sprayed red sealant at the head of a wall" style="background:linear-gradient(180deg,#d98a78 0%,#e7e2dc 40%,#ece9e4 100%)"></div></div><p>Head of Wall Joints</p></div>
<div class="svc" style="left:406px;top:719px"><div class="frame oct"><div class="photo oct" role="img" aria-label="Pipe with collar through a floor penetration" style="background:linear-gradient(135deg,#8e95c4,#c9cbd2 50%,#d97a5c 80%,#a4a8c0)"></div></div><p>Through Penetrations</p></div>
<div class="svc" style="left:611px;top:719px"><div class="frame oct"><div class="photo oct" role="img" aria-label="Curtain wall slab edge seal" style="background:linear-gradient(160deg,#c6d8e4,#8ea8b8 55%,#6d8594)"></div></div><p>Curtain Wall/Slab Edge</p></div>
<div class="svc" style="left:816px;top:719px"><div class="frame oct"><div class="photo oct" role="img" aria-label="Wrapped grease duct in a ceiling" style="background:linear-gradient(135deg,#3c3d40,#9a9ca0 50%,#2b2c2e)"></div></div><p>Grease &amp; Fume<br>Duct Protection</p></div>

<a class="btn" href="https://ridgelineflameguard.example/contact/" style="left:534px;top:966px;width:132px;height:29px">Inquiry Now</a>

<div class="divider"></div>
<h2 class="section-title display" style="top:1130px">How Firestopping Works</h2>
<p class="section-sub" style="top:1160px">Educational Video by Kestrel</p>
<div class="video" role="img" aria-label="Video still: firestop collar being fitted around pipes in a test wall">
  <svg class="play" viewBox="0 0 50 34"><path d="M20 11l12 6-12 6z" fill="#fff"/></svg>
</div>

<svg class="abs" style="left:0;top:1600px" width="1200" height="480" viewBox="0 1600 1200 480">
  <polygon points="0,1647 895,1627 1200,1674 1200,1995 335,2062 0,1985" fill="#2c3452"/>
  <polygon points="170,1688 605,1682 347,1712" fill="#fff"/>
  <polygon points="170,1688 347,1712 605,1682 347,1740" fill="#4a5fae"/>
  <polygon points="620,2009 889,1965 1087,1985 889,1975" fill="#e30613"/>
</svg>
<div class="cta-photo" role="img" aria-label="Construction worker in hard hat and orange vest on the phone holding plans"></div>
<h2 class="cta-title display">Get in touch today</h2>
<a class="btn" href="https://ridgelineflameguard.example/contact/" style="left:375px;top:1915px;width:126px;height:29px">Contact Us</a>

<h2 class="section-title display" style="top:2130px">Our Manufacturer</h2>
<svg class="arrow" style="left:166px" viewBox="0 0 20 20"><circle cx="10" cy="10" r="8.5" fill="none" stroke="#bbb"/><path d="M11.5 6l-4 4 4 4" fill="none" stroke="#bbb" stroke-width="1.3"/></svg>
<div class="maker oct" style="left:203px"><div class="face oct"><span class="name" style="color:#e30613">Kestrel</span></div></div>
<div class="maker oct" style="left:366px"><div class="face oct"><span class="name" style="color:#2a2b2f">Norvane</span></div></div>
<div class="maker oct" style="left:528px"><div class="face oct"><svg width="84" height="84" viewBox="0 0 84 84" role="img" aria-label="Accredited contractor badge"><circle cx="42" cy="42" r="40" fill="#e30613"/></svg></div></div>
<div class="maker oct" style="left:691px"><div class="face oct"><span class="name" style="color:#555">Halden<br>Materials</span></div></div>
<div class="maker oct" style="left:853px"><div class="face oct"><span class="name" style="color:#1f4fa2">Corwick<br>Seal</span></div></div>
<svg class="arrow" style="left:1016px" viewBox="0 0 20 20"><circle cx="10" cy="10" r="8.5" fill="none" stroke="#e30613"/><path d="M8.5 6l4 4-4 4" fill="none" stroke="#e30613" stroke-width="1.3"/></svg>

<svg class="abs" style="left:0;top:2400px" width="1200" height="400" viewBox="0 2400 1200 400">
  <polygon points="140,2526 697,2405 1120,2531 697,2440" fill="#4a5fae"/>
  <polygon points="0,2558 697,2440 1200,2558 1200,2800 0,2800" fill="#2a2b2f"/>
</svg>
<footer>
  <div class="footer-brand">
    <span class="brand-name">Ridgeline Flameguard</span>
    <div class="tag">FIRESTOPPING, INC • EXPANSION JOINTS</div>
  </div>

  <h3 class="col-head" style="left:151px">Conatct Info</h3>
  <svg class="icon" style="top:2644px" viewBox="0 0 13 13"><path d="M6.5 1a4 4 0 0 0-4 4c0 3 4 7 4 7s4-4 4-7a4 4 0 0 0-4-4z" fill="none" stroke="#e30613" stroke-width="1.4"/><circle cx="6.5" cy="5" r="1.3" fill="#e30613"/></svg>
  <p class="f-text" style="left:173px;top:2633px">418 W. Alder Court<br>Fullerton, CA 92831</p>
  <svg class="icon" style="top:2682px" viewBox="0 0 13 13"><path d="M3 1l2 3-1.2 1.3a7 7 0 0 0 4 4L9 8l3 2-1 2c-5 0-10-5-10-10z" fill="#e30613"/></svg>
  <p class="f-text" style="left:173px;top:2679px">(555) 014-2281</p>
  <svg class="icon" style="top:2709px" viewBox="0 0 13 13"><rect x="1" y="4" width="11" height="8" rx="1" fill="#e30613"/><rect x="3" y="1" width="7" height="4" fill="none" stroke="#e30613"/></svg>
  <p class="f-text" style="left:173px;top:2706px">(555) 014-2290</p>
  <svg class="icon" style="top:2736px" viewBox="0 0 13 13"><rect x="3" y="0.7" width="7" height="11.6" rx="1.2" fill="none" stroke="#e30613" stroke-width="1.4"/><circle cx="6.5" cy="10" r=".8" fill="#e30613"/></svg>
  <p class="f-text" style="left:173px;top:2733px">(555) 014-2307</p>

  <h3 class="col-head" style="left:373px">Quick Link</h3>
  <a class="f-link" href="#" style="top:2634px">Home</a>
  <a class="f-link" href="#" style="top:2657px">Who We Are</a>
  <a class="f-link current" href="#" style="top:2680px">What We Do</a>
  <a class="f-link" href="https://ridgelineflameguard.example/contact/" style="top:2704px">Contact</a>
  <p class="abs" style="left:373px;top:2734px;font-family:'Syncopate',sans-serif;font-weight:700;font-size:11px;color:#fff"><span style="color:#e30613">License</span> #400217</p>

  <h3 class="col-head" style="left:568px">Newsletter</h3>
  <p class="f-text" style="left:567px;top:2627px">Join our newsletter to stay updated<br>about our latest news and articles.</p>
  <div class="email">Your email address*</div>
  <a class="btn" href="#" style="left:565px;top:2711px;width:156px;height:28px">Subscribe Now</a>

  <svg class="badge" style="top:2611px" width="150" height="55" viewBox="0 0 150 55" role="img" aria-label="Safety listing badge"><circle cx="27" cy="27" r="26" fill="#e30613"/><rect x="62" y="14" width="80" height="26" rx="3" fill="#fff"/></svg>
  <svg class="badge" style="top:2677px" width="150" height="57" viewBox="0 0 150 57" role="img" aria-label="Small business certification badge"><circle cx="28" cy="28" r="27" fill="#fff"/><rect x="62" y="16" width="80" height="24" rx="3" fill="#fff"/></svg>

  <div class="legal">
    <p>© 2023 Ridgeline Flameguard. All Right Reserved</p>
    <a class="social" href="#" aria-label="Professional network profile" style="left:992px"></a>
    <a class="social" href="#" aria-label="Photo feed" style="left:1015px"></a>
    <a class="social" href="#" aria-label="Video channel" style="left:1038px"></a>
  </div>
</footer>

</body>
</html>
```